Consulting company business cards

We have a base design, but would be willing to update. We have a new logo/"tag" that needs to be added. Current business card design is attached for reference into our "style."

Industry/Entity Type

Business

Contact Information for Business Card

Should contain name and title, office number, mobile number if appropriate, e-mail, website, physical address, and company logo.

Font styles to use
Other font styles liked:
• See current card design on DrovankBCard

Colors
0455a3
85acd3
aaaaaa

Requirements
Must have
• Our colors are navy blue, gray, and a lighter blue
Nice to have
• Design that I can easily drop in new names/titles as we hire employees.

```html
<!DOCTYPE html>
<html lang="en">
<head>
<meta charset="utf-8">
<title>Harlow Business Cards</title>
<link href="https://fonts.googleapis.com/css2?family=Jost:wght@400;500&family=Oswald:wght@300;700&display=swap" rel="stylesheet">
<style>
  :root {
    --navy: #0455a3;
    --light-blue: #85acd3;
    --gray: #aaaaaa;
    --white: #ffffff;
    --backdrop: #3a3d42;
  }
  html, body {
    margin: 0;
    padding: 0;
    width: 1200px;
    height: 900px;
    overflow: hidden;
    background: var(--backdrop);
  }
  .canvas {
    position: relative;
    width: 1200px;
    height: 900px;
  }
  .card {
    position: absolute;
    width: 525px;
    height: 300px;
    border-radius: 4px;
    overflow: hidden;
    box-shadow: 0 10px 30px rgba(0,0,0,0.35);
  }
  /* Front: contact side */
  .card-front {
    left: 70px;
    top: 130px;
    background: var(--white);
    font-family: "Jost", sans-serif;
  }
  .mark-area {
    position: absolute;
    left: 55px;
    top: 85px;
    width: 170px;
    height: 170px;
    border-radius: 50%;
    background: var(--light-blue);
  }
  .identity {
    position: absolute;
    left: 250px;
    top: 34px;
    color: var(--navy);
    line-height: 1.1;
  }
  .identity .job-title {
    font-size: 15px;
    font-weight: 400;
  }
  .identity .person-name {
    font-size: 20px;
    font-weight: 500;
  }
  .contact-band {
    position: absolute;
    right: 0;
    height: 32px;
    border-radius: 16px 0 0 16px;
    display: flex;
    align-items: center;
    color: var(--white);
    font-size: 14px;
    line-height: 1;
  }
  .contact-band.navy { background: var(--navy); }
  .contact-band.light { background: var(--light-blue); }
  .contact-band svg {
    width: 18px;
    height: 18px;
    margin: 0 12px 0 10px;
    flex: none;
  }
  .contact-band.address {
    height: 38px;
    border-radius: 19px 0 0 19px;
    font-size: 12.5px;
    line-height: 1.05;
  }
  /* Back: brand side */
  .card-back {
    left: 610px;
    top: 450px;
    background: var(--navy);
    color: var(--white);
  }
  .brand {
    position: absolute;
    left: 0;
    right: 0;
    top: 78px;
    text-align: center;
  }
  .brand-row {
    display: flex;
    align-items: center;
    justify-content: center;
    gap: 16px;
  }
  .brand-name {
    font-family: "Oswald", sans-serif;
    font-weight: 700;
    font-size: 92px;
    line-height: 1;
    letter-spacing: 2px;
    text-transform: uppercase;
  }
  .brand-dot {
    width: 62px;
    height: 62px;
    border-radius: 50%;
    background: var(--white);
  }
  .tagline {
    margin-top: 8px;
    font-family: "Oswald", sans-serif;
    font-weight: 300;
    font-size: 19px;
    letter-spacing: 4px;
    text-transform: uppercase;
  }
</style>
</head>
<body>
<div class="canvas">

  <section class="card card-front">
    <div class="mark-area" role="img" aria-label="Company mark area in light blue"></div>

    <div class="identity">
      <div class="job-title">Title</div>
      <div class="person-name">Name and Surname</div>
    </div>

    <div class="contact-band navy" style="top:92px; left:238px;">
      <svg viewBox="0 0 18 18" aria-hidden="true"><rect x="5" y="1.5" width="8" height="15" rx="1.5" fill="none" stroke="#fff" stroke-width="1.5"/><line x1="8" y1="14" x2="10" y2="14" stroke="#fff" stroke-width="1.5"/></svg>
      mobile number
    </div>
    <div class="contact-band light" style="top:128px; left:262px;">
      <svg viewBox="0 0 18 18" aria-hidden="true"><path d="M4 2 L7 2 L8 6 L6 7.5 Q7.5 11 10.5 12 L12 10 L16 11 L16 14 Q16 16 14 16 Q4 15 2 4 Q2 2 4 2 Z" fill="#fff"/></svg>
      office number
    </div>
    <div class="contact-band navy" style="top:164px; left:286px;">
      <svg viewBox="0 0 18 18" aria-hidden="true"><rect x="1.5" y="4" width="15" height="10" rx="1" fill="#fff"/><polyline points="1.5,4 9,10 16.5,4" fill="none" stroke="#0455a3" stroke-width="1.3"/></svg>
      e-mail
    </div>
    <div class="contact-band light" style="top:200px; left:310px;">
      <svg viewBox="0 0 18 18" aria-hidden="true"><g fill="none" stroke="#fff" stroke-width="1.2"><circle cx="9" cy="9" r="7"/><ellipse cx="9" cy="9" rx="3" ry="7"/><line x1="2" y1="9" x2="16" y2="9"/><line x1="3" y1="5.5" x2="15" y2="5.5"/><line x1="3" y1="12.5" x2="15" y2="12.5"/></g></svg>
      web site
    </div>
    <div class="contact-band navy address" style="top:236px; left:334px;">
      <svg viewBox="0 0 18 18" aria-hidden="true"><path d="M9 1.5 Q14.5 1.5 14.5 7 Q14.5 11 9 16.5 Q3.5 11 3.5 7 Q3.5 1.5 9 1.5 Z" fill="#fff"/><circle cx="9" cy="7" r="2.2" fill="#0455a3"/></svg>
      <span>physical<br>address</span>
    </div>
  </section>

  <section class="card card-back">
    <div class="brand">
      <div class="brand-row">
        <span class="brand-name">Harlow</span>
        <span class="brand-dot" aria-hidden="true"></span>
      </div>
      <div class="tagline">A Cloud Consulting Company</div>
    </div>
  </section>

</div>
</body>
</html>
```